Minimalist Sign Design (24” X 24”)

I am wanting to redesign our yard signs to be very clean, attractive, eye catching, and readable (imagine driving by a home with a sign In yard). We paint homes. I am hoping to have a design that incorporates our brand colors in a clean, professional way that represents our company. Clean, concise, easily read from a distance.

Target Market(s)

Homeowners

Industry/Entity Type

Painting And Decorating

Font styles to use
Sans Serif

Requirements
Must have
• Phone Number: (739) 418-5067
• Free Consultations
• Makeover in progress!
• Brand colors:
• Hunter Green: #355e3b
• Black
• White
Nice to have
• Would like the hunter green to he background color of sign. Can make logo white to stand out with the green.
Should not have
• Too busy or unable to read text

```html
<!DOCTYPE html>
<html lang="en">
<head>
<meta charset="utf-8">
<title>Meridian Painting — Yard Sign</title>
<link href="https://fonts.googleapis.com/css2?family=Montserrat:wght@500;600;700&display=swap" rel="stylesheet">
<style>
  :root {
    --hunter-green: #355e3b;
    --ink: #0a0a0a;
    --frame: #231f20;
    --paper: #ffffff;
  }
  * { margin: 0; padding: 0; box-sizing: border-box; }
  html, body {
    width: 1200px;
    height: 1200px;
    overflow: hidden;
    background: var(--frame);
    font-family: "Montserrat", sans-serif;
  }
  .sign {
    position: absolute;
    left: 141px;
    top: 141px;
    width: 918px;
    height: 918px;
    background: var(--paper);
  }
  .brand {
    position: absolute;
    left: 0;
    top: 60px;
    width: 100%;
    height: 520px;
    display: flex;
    flex-direction: column;
    align-items: center;
    justify-content: center;
    gap: 40px;
  }
  .brand-mark {
    width: 300px;
    height: 300px;
  }
  .brand-name {
    font-size: 34px;
    font-weight: 500;
    letter-spacing: 12px;
    color: var(--ink);
    text-transform: uppercase;
    padding-left: 12px;
  }
  .phone-line {
    position: absolute;
    left: 52px;
    top: 628px;
    display: flex;
    align-items: center;
    gap: 18px;
  }
  .phone-icon {
    width: 68px;
    height: 68px;
    flex: none;
  }
  .phone-number {
    font-size: 94px;
    font-weight: 700;
    color: var(--hunter-green);
    line-height: 1;
    letter-spacing: 1px;
  }
  .offer {
    position: absolute;
    left: 0;
    top: 728px;
    width: 100%;
    text-align: center;
    font-size: 57px;
    font-weight: 600;
    color: var(--ink);
    line-height: 1;
  }
  .status-band {
    position: absolute;
    left: 0;
    bottom: 0;
    width: 100%;
    height: 110px;
    background: var(--hunter-green);
    display: flex;
    align-items: center;
    justify-content: center;
    font-size: 58px;
    font-weight: 700;
    line-height: 1;
    gap: 18px;
  }
  .status-band .lead { color: var(--paper); }
  .status-band .tail { color: var(--ink); }
</style>
</head>
<body>
  <main class="sign">
    <section class="brand">
      <svg class="brand-mark" viewBox="0 0 300 300" aria-hidden="true">
        <circle cx="150" cy="150" r="145" fill="none" stroke="var(--ink)" stroke-width="5"/>
      </svg>
      <div class="brand-name">Meridian Painting</div>
    </section>

    <div class="phone-line">
      <svg class="phone-icon" viewBox="0 0 68 68" aria-hidden="true">
        <circle cx="34" cy="34" r="34" fill="var(--hunter-green)"/>
        <path d="M22 17c2-1 4 0 5 2l3 7c1 2 0 3-1 4l-2 2c2 5 5 8 10 10l2-2c1-1 3-2 4-1l7 3c2 1 3 3 2 5l-2 4c-1 2-3 3-6 2-13-3-23-13-26-26-1-3 0-5 2-6z" fill="var(--paper)"/>
        <path d="M38 22a9 9 0 0 1 9 9M38 15a16 16 0 0 1 16 16" fill="none" stroke="var(--paper)" stroke-width="2.5" stroke-linecap="round"/>
      </svg>
      <span class="phone-number">(739) 418-5067</span>
    </div>

    <p class="offer">FREE CONSULTATION</p>

    <div class="status-band">
      <span class="lead">MAKEOVER</span>
      <span class="tail">IN PROGRESS!</span>
    </div>
  </main>
</body>
</html>
```